PROPERTY DEVELOPERS - LOGO & STATIONERY

We require a new logo design for a property development and sales company in Sydney, Australia.

We source land, build and sell residential & commercial investment properties including apartment buildings, townhouses, house and land packages in estates and retail shops.

We sell to local and overseas markets therefore the design needs to be a corporate effective global logo that would also suit the Asian market.

The company name is Corvane and we have been operating for 11 years and have been involved with over 5,000 properties. The focus should be on our company name Corvane with the word property as the word to explain ourselves.

This brief includes the logo design, business cards, letterhead, envelopes, with compliments slips and address label stickers.

We look forward to receiving exciting new designs.
All the best.

Reason: Designer who we were going to choose had their account closed.  Need some more options!

Property

Corvane Property

```html
<!DOCTYPE html>
<html lang="en">
<head>
<meta charset="utf-8">
<title>Corvane Property – Stationery</title>
<link rel="stylesheet" href="https://fonts.googleapis.com/css2?family=Mulish:wght@400;700&display=swap">
<style>
  :root {
    --ink: #022b2d;
    --accent: #f7941d;
    --paper: #ffffff;
    --edge: #9a9a9a;
  }
  * { margin: 0; padding: 0; box-sizing: border-box; }
  html, body { width: 849px; height: 1200px; overflow: hidden; background: var(--paper); }
  body { position: relative; font-family: "Mulish", "Century Gothic", sans-serif; color: var(--ink); }

  .piece { position: absolute; background: var(--paper); border: 1px solid var(--edge); overflow: hidden; }
  .band { position: absolute; }
  .band--accent { background: var(--accent); }
  .band--ink { background: var(--ink); }

  .brand-name {
    position: absolute; display: flex; align-items: center; justify-content: center;
    gap: 8px; text-align: center; font-weight: 700; color: var(--ink); line-height: 1.1;
  }
  .brand-square { flex: none; background: var(--ink); }

  .address { position: absolute; line-height: 16.7px; font-size: 12px; }
  .address b { font-weight: 700; }
  .dot { color: var(--accent); padding: 0 3px; }

  /* Compliments slip */
  .slip { left: 0; top: 0; width: 827px; height: 390px; }
  .slip-title { position: absolute; left: 40px; top: 96px; font-size: 18px; font-weight: 400; }
  .slip-title strong { font-weight: 700; }

  /* Business card */
  .card { left: 95px; top: 443px; width: 335px; height: 218px; }
  .card .address { font-size: 10px; line-height: 15.2px; }
  .card-person { position: absolute; left: 17px; top: 159px; font-size: 12.5px; }
  .card-person .role { display: block; font-size: 10px; margin-top: 3px; }

  /* Standalone mark area */
  .brand-large { left: 415px; top: 738px; width: 316px; height: 317px; font-size: 38px; }
</style>
</head>
<body>

  <section class="piece slip" aria-label="With compliments slip">
    <div class="band band--accent" style="left:0;top:0;width:566px;height:25px"></div>
    <div class="band band--ink" style="left:566px;top:0;width:261px;height:25px"></div>
    <div class="band band--ink" style="left:801px;top:0;width:26px;height:305px"></div>
    <div class="band band--accent" style="left:801px;top:305px;width:26px;height:85px"></div>

    <h1 class="slip-title">With <strong>Compliments</strong></h1>

    <div class="brand-name" style="left:548px;top:52px;width:162px;height:143px;font-size:20px">
      Corvane Property
    </div>

    <address class="address" style="left:566px;top:208px;font-style:normal">
      Corvane Property<span class="dot">•</span>1234 Street Name<br>
      County of Origin<span class="dot">•</span>Area of Town<br>
      State<span class="dot">•</span>ZIP 1234<br>
      <b>Tel:</b> 01234 5678900 <b>Fax:</b> 01234 6789011<br>
      <b>email:</b> sales@corvaneproperty.co.au<br>
      www.corvaneproperty.com
    </address>
  </section>

  <section class="piece card" aria-label="Business card">
    <div class="band band--accent" style="left:0;top:0;width:147px;height:15px"></div>
    <div class="band band--ink" style="left:147px;top:0;width:188px;height:15px"></div>
    <div class="band band--ink" style="left:321px;top:0;width:14px;height:162px"></div>
    <div class="band band--accent" style="left:321px;top:162px;width:14px;height:56px"></div>

    <div class="brand-name" style="left:8px;top:32px;width:110px;height:107px;font-size:15px">
      Corvane Property
    </div>

    <p class="card-person"><b>Maren</b> Corvane<span class="role">Job Title Description</span></p>

    <address class="address" style="left:147px;top:49px;font-style:normal">
      Corvane Property<br>
      1234 Street Name<br>
      County of Origin<br>
      Area of Town<span class="dot">•</span>State<span class="dot">•</span>ZIP 1234<br>
      <b>Tel:</b> 01234 5678900<br>
      <b>Fax:</b> 01234 6789011
    </address>
    <address class="address" style="left:147px;top:160px;font-style:normal">
      <b>email:</b> sales@corvaneproperty.co.au<br>
      <b>www</b>.corvaneproperty.com
    </address>
  </section>

  <div class="brand-name brand-large">Corvane Property</div>

</body>
</html>
```